Need image design for a Facebook post promo

We need a Facebook suitable image for Facebook promotion showcasing the award winners of a book competition.

The awards took place at the Writers Page Premiere and Fair. we have six awards winners and we want to display the winning authors names and photos and book images on the design.

We want our logo (WPPF) and the logo of our major sponsor TRS Press to be prominent on the design.

I will attach the logos plus a sample flyer of our event to get a feel of the theme for the event. I will also attach the photo names of the winners.

Link for authors photos and books (6):

https://files.sharevault.example/folders/7pQ2xLm9RtY4vBn8KcW3zHj5DfG6sAe1?usp=sharing

Please display our website: pagefairnest.com.au

```html
<!DOCTYPE html>
<html lang="en">
<head>
<meta charset="utf-8">
<title>Writers Page Premiere and Fair 2022 – Award Winners</title>
<link href="https://fonts.googleapis.com/css2?family=Montserrat:wght@300;400;600;700;800&family=Sarabun:wght@600&display=swap" rel="stylesheet">
<style>
  :root {
    --navy: #003552;
    --navy-deep: #0e3450;
    --gold: #edb04a;
    --gold-light: #f8cb8c;
    --gold-fold: #c98e2e;
    --cream: #fff1d6;
    --white: #ffffff;
  }
  * { margin: 0; padding: 0; box-sizing: border-box; }
  html, body { width: 1200px; height: 1200px; overflow: hidden; background: var(--navy); }
  .poster {
    position: relative; width: 1200px; height: 1200px;
    background: var(--navy); font-family: 'Montserrat', sans-serif; overflow: hidden;
  }
  .header-band {
    position: absolute; left: 0; top: 0; width: 1200px; height: 215px;
    background: linear-gradient(90deg, #ffffff 0%, #b9c2c9 22%, #5d7283 45%, #113d5a 70%, var(--navy) 100%);
    clip-path: polygon(0 0, 100% 0, 100% 162px, 0 214px);
  }
  .event-title {
    position: absolute; left: 59px; top: 30px;
    color: var(--navy-deep); font-size: 47px; line-height: 50px; letter-spacing: 1px;
  }
  .event-title .strong { display: block; font-weight: 700; }
  .event-title .light { display: block; font-weight: 300; }
  .brand-mark {
    position: absolute; color: var(--white);
    font-family: 'Montserrat', sans-serif; font-weight: 800; letter-spacing: 1px;
  }
  .brand-mark.host { left: 836px; top: 72px; font-size: 34px; }
  .brand-mark.sponsor { left: 1002px; top: 76px; font-size: 26px; }
  .headline {
    position: absolute; left: 0; width: 1200px; top: 250px; text-align: center;
    color: var(--gold); font-weight: 700; font-size: 73px; letter-spacing: 4px; line-height: 90px;
  }
  .tagline {
    position: absolute; left: 0; width: 1200px; top: 343px; text-align: center;
    color: var(--white); font-weight: 700; font-size: 30px; letter-spacing: 0.5px;
  }
  .tagline em { font-style: normal; color: var(--gold); }
  .award-card { position: absolute; width: 484px; height: 174px; }
  .award-card.col-left { left: 93px; }
  .award-card.col-right { left: 630px; }
  .award-card.row-1 { top: 427px; }
  .award-card.row-2 { top: 667px; }
  .award-card.row-3 { top: 907px; }
  .tab-light { fill: var(--gold-light); }
  .tab-fold { fill: var(--gold-fold); }
  .category-band { fill: var(--gold); }
  .category-text { fill: var(--cream); font-family: 'Montserrat', sans-serif; font-weight: 600; font-size: 26px; }
  .category-text.long { font-size: 23px; }
  .hex-frame { fill: var(--white); stroke: var(--gold); stroke-width: 6; }
  .name-band { fill: var(--navy); stroke: var(--gold); stroke-width: 5; }
  .title-band { fill: var(--white); }
  .winner-name { fill: var(--white); font-family: 'Sarabun', sans-serif; font-weight: 600; font-size: 31px; letter-spacing: 0.5px; }
  .book-title { fill: var(--navy); font-family: 'Montserrat', sans-serif; font-weight: 700; font-size: 19px; letter-spacing: 0.5px; }
  .website {
    position: absolute; right: 38px; top: 1140px;
    color: var(--white); font-weight: 300; font-size: 31px; letter-spacing: 1.5px;
  }
</style>
</head>
<body>
<svg width="0" height="0" style="position:absolute" aria-hidden="true">
  <defs>
    <linearGradient id="tone-warm" x1="0" y1="0" x2="0" y2="1"><stop offset="0" stop-color="#e7c2a8"/><stop offset="1" stop-color="#3f8c55"/></linearGradient>
    <linearGradient id="tone-dark" x1="0" y1="0" x2="0" y2="1"><stop offset="0" stop-color="#e9d2c2"/><stop offset="1" stop-color="#2a2a2e"/></linearGradient>
    <linearGradient id="tone-fair" x1="0" y1="0" x2="0" y2="1"><stop offset="0" stop-color="#f1dcb8"/><stop offset="1" stop-color="#45403c"/></linearGradient>
    <linearGradient id="tone-grey" x1="0" y1="0" x2="0" y2="1"><stop offset="0" stop-color="#e8c8b4"/><stop offset="1" stop-color="#8a8e95"/></linearGradient>
    <linearGradient id="tone-suit" x1="0" y1="0" x2="0" y2="1"><stop offset="0" stop-color="#c9a088"/><stop offset="1" stop-color="#1f2a40"/></linearGradient>
    <linearGradient id="tone-jacket" x1="0" y1="0" x2="0" y2="1"><stop offset="0" stop-color="#e3c1aa"/><stop offset="1" stop-color="#4b4a4a"/></linearGradient>
  </defs>
</svg>

<main class="poster">
  <div class="header-band"></div>
  <h1 class="event-title">
    <span class="strong">WRITERS PAGE</span>
    <span class="strong">PREMIERE AND</span>
    <span class="light">FAIR 2022</span>
  </h1>
  <div class="brand-mark host">WPPF</div>
  <div class="brand-mark sponsor">TRS Press</div>

  <h2 class="headline">AWARD WINNERS</h2>
  <p class="tagline">TURN <em>YOUR BOOK</em> INTO A <em>PROFIT GENERATOR</em></p>

  <!-- Book of the Year – Gold -->
  <svg class="award-card col-left row-1" viewBox="0 0 780 280">
    <polygon class="tab-light" points="70,2 200,2 240,70 110,70"/>
    <polygon class="tab-fold" points="180,70 240,70 210,98"/>
    <polygon class="category-band" points="210,30 690,30 730,98 210,98 240,70"/>
    <text class="category-text" x="265" y="72">BOOK OF THE YEAR - GOLD</text>
    <polygon class="name-band" points="290,114 728,114 766,180 330,180"/>
    <polygon class="title-band" points="300,180 645,180 612,242 305,242"/>
    <text class="winner-name" x="360" y="156">Maren Holloway</text>
    <text class="book-title" x="360" y="218">TRADE</text>
    <polygon class="hex-frame" points="3,177 55,79 182,79 234,177 182,275 55,275"/>
    <polygon role="img" aria-label="Portrait photo of Maren Holloway" fill="url(#tone-warm)" points="28,177 68,98 170,98 210,177 170,270 68,270"/>
    <polygon class="hex-frame" points="212,178 240,112 310,112 338,178 310,245 240,245"/>
    <rect role="img" aria-label="Book cover of TRADE" x="238" y="130" width="64" height="94" fill="url(#tone-warm)"/>
  </svg>

  <!-- Education -->
  <svg class="award-card col-right row-1" viewBox="0 0 780 280">
    <polygon class="tab-light" points="70,2 200,2 240,70 110,70"/>
    <polygon class="tab-fold" points="180,70 240,70 210,98"/>
    <polygon class="category-band" points="210,30 690,30 730,98 210,98 240,70"/>
    <text class="category-text" x="265" y="72">EDUCATION</text>
    <polygon class="name-band" points="290,114 728,114 766,180 330,180"/>
    <polygon class="title-band" points="300,180 645,180 612,242 305,242"/>
    <text class="winner-name" x="360" y="156">Daria Levant</text>
    <text class="book-title" x="360" y="218">TRADE</text>
    <polygon class="hex-frame" points="3,177 55,79 182,79 234,177 182,275 55,275"/>
    <polygon role="img" aria-label="Portrait photo of Daria Levant" fill="url(#tone-dark)" points="28,177 68,98 170,98 210,177 170,270 68,270"/>
    <polygon class="hex-frame" points="212,178 240,112 310,112 338,178 310,245 240,245"/>
    <rect role="img" aria-label="Book cover of TRADE" x="238" y="130" width="64" height="94" fill="url(#tone-dark)"/>
  </svg>

  <!-- Book of the Year – Silver -->
  <svg class="award-card col-left row-2" viewBox="0 0 780 280">
    <polygon class="tab-light" points="70,2 200,2 240,70 110,70"/>
    <polygon class="tab-fold" points="180,70 240,70 210,98"/>
    <polygon class="category-band" points="210,30 690,30 730,98 210,98 240,70"/>
    <text class="category-text" x="265" y="72">BOOK OF THE YEAR - SILVER</text>
    <polygon class="name-band" points="290,114 728,114 766,180 330,180"/>
    <polygon class="title-band" points="300,180 645,180 612,242 305,242"/>
    <text class="winner-name" x="360" y="156">Corinne Ashby</text>
    <text class="book-title" x="360" y="218">THE MINDFUL CHIEF</text>
    <polygon class="hex-frame" points="3,177 55,79 182,79 234,177 182,275 55,275"/>
    <polygon role="img" aria-label="Portrait photo of Corinne Ashby" fill="url(#tone-fair)" points="28,177 68,98 170,98 210,177 170,270 68,270"/>
    <polygon class="hex-frame" points="212,178 240,112 310,112 338,178 310,245 240,245"/>
    <rect role="img" aria-label="Book cover of The Mindful Chief" x="238" y="130" width="64" height="94" fill="#f08a24"/>
  </svg>

  <!-- Leadership & Management -->
  <svg class="award-card col-right row-2" viewBox="0 0 780 280">
    <polygon class="tab-light" points="70,2 200,2 240,70 110,70"/>
    <polygon class="tab-fold" points="180,70 240,70 210,98"/>
    <polygon class="category-band" points="210,30 690,30 730,98 210,98 240,70"/>
    <text class="category-text" x="265" y="72">LEADERSHIP &amp; MANAGEMENT</text>
    <polygon class="name-band" points="290,114 728,114 766,180 330,180"/>
    <polygon class="title-band" points="300,180 645,180 612,242 305,242"/>
    <text class="winner-name" x="360" y="156">Owen Carraway</text>
    <text class="book-title" x="360" y="218">TRADE</text>
    <polygon class="hex-frame" points="3,177 55,79 182,79 234,177 182,275 55,275"/>
    <polygon role="img" aria-label="Portrait photo of Owen Carraway" fill="url(#tone-grey)" points="28,177 68,98 170,98 210,177 170,270 68,270"/>
    <polygon class="hex-frame" points="212,178 240,112 310,112 338,178 310,245 240,245"/>
    <rect role="img" aria-label="Book cover of TRADE" x="238" y="130" width="64" height="94" fill="#1fa8c9"/>
  </svg>

  <!-- Book of the Year – Bronze -->
  <svg class="award-card col-left row-3" viewBox="0 0 780 280">
    <polygon class="tab-light" points="70,2 200,2 240,70 110,70"/>
    <polygon class="tab-fold" points="180,70 240,70 210,98"/>
    <polygon class="category-band" points="210,30 690,30 730,98 210,98 240,70"/>
    <text class="category-text" x="265" y="72">BOOK OF THE YEAR - BRONZE</text>
    <polygon class="name-band" points="290,114 728,114 766,180 330,180"/>
    <polygon class="title-band" points="300,180 645,180 612,242 305,242"/>
    <text class="winner-name" x="360" y="156">Ravi Sethwick</text>
    <text class="book-title" x="360" y="218">UNLEARNED</text>
    <polygon class="hex-frame" points="3,177 55,79 182,79 234,177 182,275 55,275"/>
    <polygon role="img" aria-label="Portrait photo of Ravi Sethwick" fill="url(#tone-suit)" points="28,177 68,98 170,98 210,177 170,270 68,270"/>
    <polygon class="hex-frame" points="212,178 240,112 310,112 338,178 310,245 240,245"/>
    <rect role="img" aria-label="Book cover of Unlearned" x="238" y="130" width="64" height="94" fill="#12233f"/>
  </svg>

  <!-- Sales & Business Performance -->
  <svg class="award-card col-right row-3" viewBox="0 0 780 280">
    <polygon class="tab-light" points="70,2 200,2 240,70 110,70"/>
    <polygon class="tab-fold" points="180,70 240,70 210,98"/>
    <polygon class="category-band" points="210,30 690,30 730,98 210,98 240,70"/>
    <text class="category-text long" x="265" y="72">SALES &amp; BUSINESS PERFORMANCE</text>
    <polygon class="name-band" points="290,114 728,114 766,180 330,180"/>
    <polygon class="title-band" points="300,180 645,180 612,242 305,242"/>
    <text class="winner-name" x="360" y="156">Lena Pritchard</text>
    <text class="book-title" x="360" y="218">TRADE</text>
    <polygon class="hex-frame" points="3,177 55,79 182,79 234,177 182,275 55,275"/>
    <polygon role="img" aria-label="Portrait photo of Lena Pritchard" fill="url(#tone-jacket)" points="28,177 68,98 170,98 210,177 170,270 68,270"/>
    <polygon class="hex-frame" points="212,178 240,112 310,112 338,178 310,245 240,245"/>
    <rect role="img" aria-label="Book cover of TRADE" x="238" y="130" width="64" height="94" fill="#e8c3a4"/>
  </svg>

  <div class="website">pagefairnest.com.au</div>
</main>
</body>
</html>
```